Stationery Design Project for Wellmind Therapy Rooms

I would like you to design a letterhead and appt cards and letterhead. i have attached our current brochure so that you can see the kind of clinic that we are - for some context.

Generally our letters will go to General Practitioners.
Appt cards to clients. The text can stay the same as current documents as attached but the design obviously needs to be totally changed.

We are a psychology clinic with several psychologists that work for me. THe psychologists come and go so I am not wanting to list their names on the stationary.

In terms of letterhead my name (dr marnie calloway) needs to be on there..eg dr marnie calloway & associates.

With envelopes we need to be discrete therefore we simply have WTR & our address.

Everything goes under the banner of Wellmind Therapy Rooms Pty Ltd.

I would like it to be consistent in theme/colours with the logo you designed and our website which has just gone live www.wellmindtherapyrooms.com.au

Target Market(s)

General practitioners, potential referrers usually in the medical/health field,

Industry/Entity Type

Clinic

Requirements
Must have
• Logo

Address Suite 4, 287 Kelmore Rd, Brinwood Vale 3172
P 9563 2418 F 9563 2419 E info@wellmindtherapyrooms.com.au
W wellmindtherapyrooms.com.au

Wellmind Therapy Rooms Pty Ltd (small font)
ABN (ill need to provide this) (small font)
Nice to have
• I really like in my website how the colours are graded in the banners...I think this gives a softer feel...so if something like that would look good in our stationary then please use that kind of technique too...but you guys are the experts.

```html
<!DOCTYPE html>
<html lang="en">
<head>
<meta charset="utf-8">
<title>Wellmind Therapy Rooms – Business and Appointment Cards</title>
<link rel="stylesheet" href="https://fonts.googleapis.com/css2?family=Lato:ital,wght@0,400;0,700;1,400&display=swap">
<style>
  :root {
    --backdrop: #eeefef;
    --slate: #7f9fb3;
    --aqua: #8fc7ca;
    --teal: #7fb0b0;
    --steel: #8a939c;
    --lilac: #bcc3e0;
    --mist: #e3e7f0;
    --ink: #505050;
    --brand-grey: #7b7b7b;
    --rule: #bdbdbd;
    --white: #ffffff;
  }
  * { margin: 0; padding: 0; box-sizing: border-box; }
  html, body { width: 1200px; height: 900px; overflow: hidden; }
  body {
    background: radial-gradient(ellipse at 50% 40%, #f7f7f7, var(--backdrop) 70%, #e4e5e5);
    font-family: "Lato", sans-serif;
    color: var(--ink);
    position: relative;
  }

  .stripe { position: absolute; display: flex; left: 0; right: 0; }
  .stripe span { flex: 1; }
  .c-slate { background: var(--slate); }
  .c-aqua { background: var(--aqua); }
  .c-teal { background: var(--teal); }
  .c-steel { background: var(--steel); }

  /* Business card */
  .business-card {
    position: absolute; left: 149px; top: 302px; width: 532px; height: 296px;
    background: linear-gradient(90deg, var(--lilac), var(--mist));
    box-shadow: 0 1px 5px rgba(0,0,0,0.25);
  }
  .business-card .stripe-top { top: 0; height: 10px; }
  .business-card .stripe-bottom { bottom: 0; height: 21px; }

  .brand { position: absolute; left: 18px; top: 48px; display: flex; align-items: center; gap: 22px; }
  .brand-dot { width: 80px; height: 80px; border-radius: 50%; background: #e8eaf2; }
  .brand-name {
    font-size: 18px; line-height: 23px; letter-spacing: 3.6px;
    text-transform: uppercase; color: var(--brand-grey); font-weight: 400;
  }

  .contact { position: absolute; top: 193px; font-size: 15px; line-height: 18px; white-space: nowrap; font-style: normal; }
  .contact-phone {
    left: 18px;
    display: grid;
    grid-template-columns: 22px auto;
  }
  .contact-phone dt { font-weight: 700; }
  .contact-address { left: 313px; }

  /* Appointment card */
  .appointment-card {
    position: absolute; left: 755px; top: 184px; width: 295px; height: 532px;
    background: var(--white);
    box-shadow: 0 1px 5px rgba(0,0,0,0.25);
  }
  .appointment-card .stripe-top { top: 0; height: 10px; }
  .appointment-card .stripe-bottom { bottom: 0; height: 21px; }

  .field-heading { position: absolute; left: 30px; font-size: 15px; color: #3f3f3f; }
  .psychologist-heading { top: 34px; }
  .psychologist-line { position: absolute; left: 30px; width: 246px; top: 74px; border-top: 1px solid var(--rule); }
  .appointments-heading { top: 92px; }

  .slot { position: absolute; left: 30px; width: 246px; height: 44px; font-size: 10px; text-transform: uppercase; }
  .slot-row { position: absolute; left: 0; display: flex; align-items: baseline; white-space: nowrap; }
  .slot-date { top: 0; width: 246px; }
  .slot-time { top: 28px; }
  .slot-line { border-bottom: 1px solid var(--rule); margin-left: 4px; height: 1px; }
  .slot-date .slot-line { flex: 1; }
  .slot-time .slot-line { width: 100px; }
  .slot-meridiem { margin-left: 7px; }

  .company { position: absolute; left: 30px; top: 413px; font-size: 11.5px; line-height: 16px; color: #444; white-space: nowrap; }
  .notice { position: absolute; left: 30px; top: 462px; font-size: 11px; line-height: 16px; font-style: italic; color: #444; white-space: nowrap; }
</style>
</head>
<body>

  <section class="business-card" aria-label="Business card">
    <div class="stripe stripe-top"><span class="c-slate"></span><span class="c-aqua"></span><span class="c-teal"></span><span class="c-steel"></span><span class="c-aqua"></span></div>

    <div class="brand">
      <div class="brand-dot"></div>
      <p class="brand-name">Wellmind<br>Therapy<br>Rooms</p>
    </div>

    <dl class="contact contact-phone">
      <dt>t</dt><dd>9563 2418</dd>
      <dt>f</dt><dd>9563 2419</dd>
      <dt>e</dt><dd>info@wellmindtherapyrooms.com.au</dd>
    </dl>
    <address class="contact contact-address">
      Suite 4, 287 Kelmore Rd<br>Brinwood Vale 3172<br>wellmindtherapyrooms.com.au
    </address>

    <div class="stripe stripe-bottom"><span class="c-slate"></span><span class="c-aqua"></span><span class="c-teal"></span><span class="c-steel"></span><span class="c-aqua"></span></div>
  </section>

  <section class="appointment-card" aria-label="Appointment card">
    <div class="stripe stripe-top"><span class="c-aqua"></span><span class="c-teal"></span><span class="c-steel"></span></div>

    <p class="field-heading psychologist-heading">Your psychologist:</p>
    <div class="psychologist-line"></div>
    <p class="field-heading appointments-heading">Your appointments:</p>

    <div class="slot" style="top:128px">
      <div class="slot-row slot-date">Date<span class="slot-line"></span></div>
      <div class="slot-row slot-time">Time<span class="slot-line"></span><span class="slot-meridiem">AM | PM</span></div>
    </div>
    <div class="slot" style="top:199px">
      <div class="slot-row slot-date">Date<span class="slot-line"></span></div>
      <div class="slot-row slot-time">Time<span class="slot-line"></span><span class="slot-meridiem">AM | PM</span></div>
    </div>
    <div class="slot" style="top:270px">
      <div class="slot-row slot-date">Date<span class="slot-line"></span></div>
      <div class="slot-row slot-time">Time<span class="slot-line"></span><span class="slot-meridiem">AM | PM</span></div>
    </div>
    <div class="slot" style="top:340px">
      <div class="slot-row slot-date">Date<span class="slot-line"></span></div>
      <div class="slot-row slot-time">Time<span class="slot-line"></span><span class="slot-meridiem">AM | PM</span></div>
    </div>

    <p class="company">Wellmind Therapy Rooms Pty Ltd<br>ABN 51 824 370 165</p>
    <p class="notice">Please note fees will be charged for missed<br>appointments without 48 hours notice.</p>

    <div class="stripe stripe-bottom"><span class="c-aqua"></span><span class="c-teal"></span><span class="c-steel"></span></div>
  </section>

</body>
</html>
```